design a word press website for a real estate law firm
home page
services page: Real estate, title
People page: 1 man 3 women
news and insights page
location page
contact us page
our story page
insights page

```html
<!DOCTYPE html>
<html lang="en">
<head>
<meta charset="utf-8">
<title>Harwell Law — Real Estate &amp; Title Counsel</title>
<link rel="stylesheet" href="https://fonts.googleapis.com/css2?family=Playfair+Display:ital,wght@0,400;1,400&family=Raleway:wght@400;500;600;700&display=swap">
<style>
:root{
  --ink:#2b2729;
  --night:#221e20;
  --panel:#262224;
  --slate:#34302f;
  --band:#2f2b2d;
  --footer:#1f1b1d;
  --mist:#e9e4e6;
  --gold:#b49b5b;
  --white:#ffffff;
  --text:#4b4548;
  --soft:#cfc9cb;
  --muted:#6e686a;
}
*{margin:0;padding:0;box-sizing:border-box}
html,body{width:1200px;height:3475px;overflow:hidden}
body{position:relative;background:var(--white);font-family:"Raleway",sans-serif;color:var(--text)}
a{text-decoration:none;color:inherit}
.abs{position:absolute}
.center{text-align:center}

/* header */
.site-header{left:0;top:0;width:1200px;height:63px;background:var(--ink)}
.brand-box{left:35px;top:9px;width:138px;height:45px;border:1px solid var(--muted);color:var(--white);font-size:19px;letter-spacing:4px;display:flex;align-items:center;justify-content:center}
.main-nav{right:165px;top:0;height:63px;display:flex;gap:40px;align-items:center}
.main-nav a{color:var(--white);font-size:10px;font-weight:700;letter-spacing:2px}
.social-top{right:52px;top:17px;display:flex;gap:4px}
.social-top span{width:30px;height:30px;border:1px solid var(--muted);border-radius:50%;color:var(--white);font-size:8px;font-weight:700;display:flex;align-items:center;justify-content:center}

/* hero */
.hero-bg{left:0;top:63px;width:1200px;height:472px;background:var(--slate)}
.hero{left:24px;top:88px;width:1152px;height:461px;background:var(--night);overflow:hidden}
.hero-photo{right:0;top:0;width:540px;height:461px;background:radial-gradient(ellipse at 50% 35%,#4a4345 0%,#2a2527 55%,var(--night) 80%)}
.hero-mark{left:111px;top:150px;width:52px;height:52px;border:3px solid var(--white)}
.hero-title{left:208px;top:148px;font-family:"Playfair Display",serif;font-weight:400;font-size:54px;letter-spacing:19px;color:var(--white);line-height:1}
.hero-tm{left:892px;top:152px;font-size:11px;color:var(--white)}
.hero-sub{left:206px;top:230px;font-family:"Playfair Display",serif;font-style:italic;font-size:26px;color:#5c5557}
.btn{font-size:10px;font-weight:700;letter-spacing:1.5px;color:var(--white);display:flex;align-items:center;justify-content:center}
.btn-gold{background:var(--gold)}
.btn-line{border:1px solid var(--muted)}
.btn-dark{background:#3e393b}

/* quote */
.avatar{border-radius:50%;background:radial-gradient(circle at 50% 40%,#6a6466 0%,#3a3537 60%,#262224 100%)}
.quote-marks{left:318px;top:640px;font-family:"Playfair Display",serif;font-size:96px;line-height:1;color:var(--gold)}
.quote-text{left:271px;top:850px;width:320px;font-family:"Playfair Display",serif;font-style:italic;font-size:16px;line-height:23px;color:var(--text)}
.quote-author{left:261px;top:939px;width:340px;font-family:"Playfair Display",serif;font-style:italic;font-size:11px;color:var(--muted)}
.statue{left:612px;top:600px;width:328px;height:462px;background:linear-gradient(160deg,#4a4446 0%,#2a2527 60%,#1c1819 100%)}

/* section titles */
.sec-title{left:0;width:1200px;font-size:26px;font-weight:500;letter-spacing:8px;color:var(--ink)}
.sec-sub{left:0;width:1200px;font-family:"Playfair Display",serif;font-style:italic;font-size:16px;color:#5c5557}

/* practice cards */
.cards{left:24px;top:1247px;width:1152px;height:458px;display:flex;gap:1px;background:var(--white)}
.card{flex:1;position:relative;background:linear-gradient(180deg,#3a3436 0%,#262224 70%,#1e1a1c 100%)}
.card-icon{position:absolute;left:50%;top:88px;width:70px;height:70px;margin-left:-35px}
.card h3{position:absolute;left:0;right:0;top:198px;font-size:13px;font-weight:700;letter-spacing:2.5px;color:var(--white);text-align:center}
.card p{position:absolute;left:58px;right:58px;top:227px;font-size:12px;line-height:20px;color:var(--white);text-align:center}
.card .btn{position:absolute;left:50%;top:337px;width:122px;height:42px;margin-left:-61px}

/* team */
.member{position:absolute;width:260px;text-align:center}
.member .avatar{width:220px;height:220px;margin:0 auto}
.member-name{margin-top:24px;font-size:12px;font-weight:700;letter-spacing:2.5px;color:var(--ink)}
.member-role{margin-top:6px;font-family:"Playfair Display",serif;font-style:italic;font-size:13px;color:var(--gold)}
.member-bio{margin:10px auto 0;width:240px;font-size:12px;line-height:20px;color:var(--text)}

/* video panel */
.dark-band{left:0;top:2709px;width:1200px;height:332px;background:var(--band)}
.team-panel{left:24px;top:2409px;width:1152px;height:476px;background:linear-gradient(120deg,#3a3537 0%,var(--panel) 55%)}
.team-title{left:24px;top:2536px;width:620px;font-size:26px;font-weight:500;letter-spacing:7px;color:var(--white)}
.team-copy{left:136px;top:2588px;width:396px;font-size:12px;line-height:20px;color:var(--soft)}
.video-frame{left:611px;top:2470px;width:504px;height:354px;background:#3a3537}
.video{left:630px;top:2488px;width:469px;height:317px;background:linear-gradient(135deg,#8a6a4a 0%,#5a4636 45%,#2e2624 100%)}
.play{left:820px;top:2603px;width:86px;height:86px;border-radius:50%;background:rgba(180,155,91,.85)}

.partners{left:110px;top:2930px;width:990px;display:flex;justify-content:space-between}
.partners span{width:150px;height:52px;background:#3c3739;border-radius:4px}

/* footer */
.site-footer{left:0;top:3041px;width:1200px;height:434px;background:var(--footer)}
.foot-mark{left:583px;top:3125px;width:34px;height:34px;border:3px solid var(--white)}
.foot-name{left:0;top:3196px;width:1200px;font-family:"Playfair Display",serif;font-size:32px;letter-spacing:14px;color:var(--white)}
.foot-copy{left:0;top:3262px;width:1200px;font-size:11px;color:var(--muted)}
.foot-social{left:459px;top:3318px;display:flex;gap:4px}
.foot-social span{width:66px;height:66px;border:1px solid #4e484a;border-radius:50%;color:var(--white);font-size:11px;font-weight:700;display:flex;align-items:center;justify-content:center}
</style>
</head>
<body>

<header class="site-header abs">
  <div class="brand-box abs">KEYSTONE</div>
  <nav class="main-nav abs">
    <a href="#">HOMEPAGE</a><a href="#">OUR STORY</a><a href="#">SERVICES</a><a href="#">PEOPLE</a><a href="#">CONTACT</a>
  </nav>
  <div class="social-top abs"><span>LI</span><span>FB</span><span>IG</span></div>
</header>

<div class="hero-bg abs"></div>
<section class="hero abs">
  <div class="hero-photo abs" role="img" aria-label="Portrait of a lawyer in a dark suit, arms crossed"></div>
  <div class="hero-mark abs"></div>
  <h1 class="hero-title abs">HARWELL LAW</h1>
  <div class="hero-tm abs">tm</div>
  <p class="hero-sub abs">Solving complex real estate, title and property issues</p>
  <a class="btn btn-gold abs" href="#" style="left:206px;top:296px;width:138px;height:51px">READ MORE</a>
  <a class="btn btn-line abs" href="#" style="left:353px;top:296px;width:150px;height:51px">EMERGENCY?</a>
</section>

<svg class="abs" style="left:0;top:1028px" width="1200" height="488" aria-hidden="true">
  <polygon points="0,0 1200,71 1200,488 0,488" fill="#e9e4e6"/>
</svg>

<div class="quote-marks abs">&#8221;</div>
<div class="avatar abs" style="left:337px;top:638px;width:188px;height:188px" role="img" aria-label="Portrait of the managing partner"></div>
<p class="quote-text abs center">Every closing rests on a clear title. We guard each deed, lease and deal from first draft to final key.</p>
<p class="quote-author abs center">- Martin Ellery Shaw</p>
<div class="statue abs" role="img" aria-label="Bronze statue of Lady Justice holding scales"></div>

<h2 class="sec-title abs center" style="top:1132px">OUR SERVICES</h2>
<p class="sec-sub abs center" style="top:1167px">Real estate and title counsel</p>

<section class="cards abs">
  <article class="card">
    <svg class="card-icon" viewBox="0 0 70 70" aria-hidden="true" fill="none" stroke="#b49b5b" stroke-width="2.5"><path d="M10 34 L35 12 L60 34"/><path d="M17 29 V60 H53 V29"/><rect x="29" y="42" width="12" height="18"/></svg>
    <h3>REAL ESTATE</h3><p>Purchases, sales and development deals for homes and commercial property.</p><a class="btn btn-dark" href="#">EXPLORE</a>
  </article>
  <article class="card">
    <svg class="card-icon" viewBox="0 0 70 70" aria-hidden="true" fill="none" stroke="#b49b5b" stroke-width="2.5"><path d="M18 8 H44 L54 18 V62 H18 Z"/><path d="M44 8 V18 H54"/><path d="M26 30 H46 M26 39 H46 M26 48 H38"/></svg>
    <h3>TITLE</h3><p>Title searches, insurance and clean transfer of ownership at every closing.</p><a class="btn btn-dark" href="#">EXPLORE</a>
  </article>
  <article class="card">
    <svg class="card-icon" viewBox="0 0 70 70" aria-hidden="true" fill="none" stroke="#b49b5b" stroke-width="2.5"><circle cx="22" cy="35" r="11"/><path d="M33 35 H62 M52 35 V45 M60 35 V43"/></svg>
    <h3>LEASING</h3><p>Drafting and review of residential and commercial leases for both sides.</p><a class="btn btn-dark" href="#">EXPLORE</a>
  </article>
  <article class="card">
    <svg class="card-icon" viewBox="0 0 70 70" aria-hidden="true" fill="none" stroke="#b49b5b" stroke-width="2.5"><path d="M35 10 V60 M22 60 H48 M14 20 H56"/><path d="M14 20 L6 40 H22 Z M56 20 L48 40 H64 Z"/></svg>
    <h3>DISPUTES</h3><p>Boundary, title and contract disputes settled in talks or in court.</p><a class="btn btn-dark" href="#">EXPLORE</a>
  </article>
</section>

<h2 class="sec-title abs center" style="top:1790px">OUR PEOPLE</h2>
<p class="sec-sub abs center" style="top:1825px">Solving your property problems</p>

<svg class="abs" style="left:0;top:1920px" width="1200" height="489" aria-hidden="true">
  <polygon points="0,55 1200,0 1200,489 0,489" fill="#e9e4e6"/>
</svg>

<div class="member" style="left:65px;top:1936px">
  <div class="avatar" role="img" aria-label="Portrait of partner Clara Bennett"></div>
  <div class="member-name">CLARA BENNETT</div>
  <div class="member-role">Managing Partner</div>
  <p class="member-bio">Leads commercial purchases and development deals across the region.</p>
</div>
<div class="member" style="left:335px;top:1906px">
  <div class="avatar" style="background:radial-gradient(circle at 50% 40%,#4a4446 0%,#1a1617 70%)" role="img" aria-label="Portrait of partner Daniel Reyes Hartley"></div>
  <div class="member-name">DANIEL REYES HARTLEY</div>
  <div class="member-role">Title Partner</div>
  <p class="member-bio">Handles title review, insurance claims and complex closings.</p>
</div>
<div class="member" style="left:605px;top:1936px">
  <div class="avatar" role="img" aria-label="Portrait of associate Nora Whitfield"></div>
  <div class="member-name">NORA WHITFIELD</div>
  <div class="member-role">Senior Associate</div>
  <p class="member-bio">Drafts and negotiates residential and commercial leases.</p>
</div>
<div class="member" style="left:875px;top:1906px">
  <div class="avatar" style="background:radial-gradient(circle at 50% 40%,#4a4446 0%,#1a1617 70%)" role="img" aria-label="Portrait of associate Priya Anand"></div>
  <div class="member-name">PRIYA ANAND</div>
  <div class="member-role">Associate</div>
  <p class="member-bio">Resolves boundary and contract disputes in talks or in court.</p>
</div>

<div class="dark-band abs"></div>
<section class="team-panel abs"></section>
<h2 class="team-title abs center">HARWELL TEAM</h2>
<p class="team-copy abs center">For three decades we have guided buyers, sellers, lenders and landlords through every stage of a property deal. From the first title search to the final signature, our team keeps each transfer clear, secure and on time.</p>
<a class="btn btn-gold abs" href="#" style="left:260px;top:2699px;width:150px;height:51px">EMERGENCY?</a>
<div class="video-frame abs"></div>
<div class="video abs" role="img" aria-label="Video still of a lawyer addressing clients in an office"></div>
<div class="play abs"></div>
<svg class="abs" style="left:853px;top:2630px" width="26" height="32" aria-hidden="true"><polygon points="0,0 26,16 0,32" fill="#ffffff"/></svg>

<div class="partners abs"><span></span><span></span><span></span><span></span><span></span></div>

<footer class="site-footer abs"></footer>
<div class="foot-mark abs"></div>
<div class="foot-name abs center">HARWELL/ASHBY</div>
<p class="foot-copy abs center">© Copyright Northfold Studio. This is a part of Keystone theme.</p>
<div class="foot-social abs"><span>IG</span><span>LI</span><span>FB</span><span>TW</span></div>

</body>
</html>
```